ALL TEXT GRAPHICS TM May 2025 for Instagram

We are looking for a series of social media graphics for Instagram (new size: 4:5 (1080 x 1350 pixels) ratio that are ALL TEXT. We want the following quotes below on each graphic; one quote per graphic. AND, In very small letters at the bottom of each graphic, add @TovaMarshOnline
The look and feel of these graphics should be complimentary to the color palette attached below; but keep them simple. But the design is up to you; at the end of this document, I provided various samples of all text graphics that I like as examples.
Target Market(s)
women looking to lose weight
Look and feel

```html
<!DOCTYPE html>
<html lang="en">
<head>
<meta charset="utf-8">
<title>Belly Won't Go Down – TM Instagram Graphic</title>
<link rel="stylesheet" href="https://fonts.googleapis.com/css2?family=Fira+Sans:wght@300;400;600;700&display=swap">
<style>
  :root {
    --bg: #ffffff;
    --ink: #111111;
    --pink: #ff1493;
    --pink-bright: #ff3399;
    --pink-deep: #cc0066;
    --white: #ffffff;
  }
  * { margin: 0; padding: 0; box-sizing: border-box; }
  html, body {
    width: 960px;
    height: 1200px;
    overflow: hidden;
    background: var(--bg);
  }
  .post {
    position: relative;
    width: 960px;
    height: 1200px;
    background: var(--bg);
    font-family: "Fira Sans", sans-serif;
    color: var(--ink);
  }
  .question {
    position: absolute;
    top: 292px;
    left: 0;
    width: 100%;
    text-align: center;
    font-weight: 300;
    font-size: 72px;
    line-height: 89px;
    letter-spacing: -1px;
  }
  .question .line { display: block; }
  .question .emphasis {
    color: var(--pink);
    font-weight: 700;
  }
  .answer {
    position: absolute;
    top: 739px;
    left: 0;
    width: 100%;
    text-align: center;
  }
  .answer .tag {
    display: inline-block;
    color: var(--white);
    font-weight: 300;
    font-size: 70px;
    line-height: 75px;
    letter-spacing: -1px;
    padding: 0 28px 0 26px;
  }
  .answer .tag-top {
    background: var(--pink-bright);
    margin-left: 35px;
  }
  .answer .tag-bottom {
    background: var(--pink-deep);
    margin-top: 14px;
    padding: 0 14px 0 16px;
    margin-left: -17px;
  }
  .handle {
    position: absolute;
    top: 1098px;
    left: 0;
    width: 100%;
    text-align: center;
    font-weight: 600;
    font-size: 15px;
    color: var(--pink-deep);
  }
</style>
</head>
<body>
  <main class="post">
    <h1 class="question">
      <span class="line">You’re doing all the</span>
      <span class="line"><span class="emphasis">“right”</span> things,</span>
      <span class="line">but your belly won’t</span>
      <span class="line">go down?</span>
    </h1>
    <div class="answer">
      <span class="tag tag-top">Here’s what</span><br>
      <span class="tag tag-bottom">you haven’t tried.</span>
    </div>
    <p class="handle">@TovaMarshOnline</p>
  </main>
</body>
</html>
```